A more modern website banner for a family-size car selling business

Hello there !

I need a new banner for our existing website.

The website :
http://www.garagevormandel.com/

The banner image :
http://www.garagevormandel.com/images/ban.jpg

Industry/Entity Type

Business

Requirements
Must have
• - Must integrate nicely with the existing design.
• - Must be a simple drop-in replacement for the existing image. Important : you can play with height, but maximum is 250px, minimum 100 px
• - Must have the name "Garage Lucien Vormandel" somewhere, readable
Nice to have
• - We would like to have a photo of a Tiko Brisk, but it's not mandatory. Also, it should not be the only picture
• - Should have at least two cars (if you put pictures of cars)
Should not have
• - Cartoonish look

```html
<!DOCTYPE html>
<html lang="fr">
<head>
<meta charset="utf-8">
<title>Garage Lucien Vormandel</title>
<link rel="stylesheet" href="https://fonts.googleapis.com/css2?family=Montserrat:wght@700&display=swap">
<style>
  :root {
    --bg: #000000;
    --car-tone: #2a2a2a;
    --car-edge: #0a0a0a;
    --stripe: rgba(255, 255, 255, 0.85);
    --scanline: rgba(0, 0, 0, 0.35);
    --title: #ffffff;
  }
  html, body {
    margin: 0;
    padding: 0;
    width: 1200px;
    height: 303px;
    overflow: hidden;
    background: var(--bg);
  }
  .banner {
    position: relative;
    width: 1200px;
    height: 303px;
    overflow: hidden;
    background: var(--bg);
  }
  .car-photo {
    position: absolute;
    left: 150px;
    top: -20px;
    width: 900px;
    height: 340px;
    background:
      radial-gradient(ellipse 45% 40% at 50% 30%, #3c3c3c 0%, transparent 70%),
      radial-gradient(ellipse 50% 55% at 50% 55%, var(--car-tone) 0%, var(--car-edge) 75%, transparent 100%);
  }
  .scanlines {
    position: absolute;
    inset: 0;
    background: repeating-linear-gradient(to bottom, transparent 0 2px, var(--scanline) 2px 3px);
  }
  .stripe-band {
    position: absolute;
    left: 20px;
    width: 1158px;
    background: repeating-linear-gradient(to bottom, var(--stripe) 0 1px, transparent 1px 3px);
  }
  .stripe-band--top { top: 89px; height: 19px; }
  .stripe-band--bottom { top: 217px; height: 18px; }
  .glow {
    position: absolute;
    left: 760px;
    top: 120px;
    width: 200px;
    height: 90px;
    background: radial-gradient(ellipse at center, rgba(255,255,255,0.35) 0%, transparent 70%);
  }
  .title {
    position: absolute;
    left: 0;
    top: 0;
    width: 1200px;
    height: 303px;
  }
  .title text {
    font-family: "Montserrat", sans-serif;
    font-weight: 700;
    font-size: 86px;
    fill: var(--title);
  }
</style>
</head>
<body>
  <div class="banner">
    <div class="car-photo" role="img" aria-label="Dark photo of the front of a car"></div>
    <div class="scanlines"></div>
    <div class="stripe-band stripe-band--top"></div>
    <div class="stripe-band stripe-band--bottom"></div>
    <div class="glow"></div>
    <svg class="title" viewBox="0 0 1200 303" aria-label="Garage Lucien Vormandel">
      <text x="31" y="193" textLength="1140" lengthAdjust="spacingAndGlyphs">GARAGE LUCIEN VORMANDEL</text>
    </svg>
  </div>
</body>
</html>
```